Need a single page vertical flyer to include in a folder of info

Need a list of things we offer with partnerships of another company
single page easy to read.

Look at www.calibrolook.com for info
include that we provide a free report from www.calibrolook.com with every complete job that is linked to www.repairvault.com for source info.

mobile services we provide
advanced driver systems (adas) calibrations
Diagnostics
Oem programming European and domestics.
collision mechanical
Wiring repair
pigtails

we service all makes and models

Email estimate to milo@r-voxauto.com for free calibro look report

important phrases, " Locally owned and operated."

"Dealership alternative."
"We help speedup your cycle time."
Phone (555) 013-4872

Target Market(s)

Business to business

Industry/Entity Type

Mobile Auto diagnostics and calibrations

Requirements
Must have
• Easy to read and to the point.
Nice to have
• Clean background with some kind of photo

```html
<!DOCTYPE html>
<html lang="en">
<head>
<meta charset="UTF-8">
<title>R-VOX Automotive Solutions – Mobile ADAS Calibration Flyer</title>
<link rel="stylesheet" href="https://fonts.googleapis.com/css2?family=Rubik:wght@500;600&family=Roboto:wght@300;400;500&family=Audiowide&family=Oxanium:wght@500;600&display=swap">
<style>
  :root{
    --navy:#2a2560;
    --gold:#e9c97c;
    --gold-dark:#c79a37;
    --gold-light:#f2dc9e;
    --yellow:#f7d23e;
    --cream:#fdf4c5;
    --white:#ffffff;
    --ink:#24214f;
  }
  *{margin:0;padding:0;box-sizing:border-box}
  html,body{width:848px;height:1200px;overflow:hidden;background:var(--white)}
  .flyer{position:relative;width:848px;height:1200px;overflow:hidden;background:var(--white);font-family:'Roboto',sans-serif}

  /* Hero */
  .hero{position:absolute;left:0;top:0;width:848px;height:530px;background:var(--navy)}
  .hero-art{position:absolute;left:0;top:0}
  .brand{position:absolute;left:38px;top:62px;display:flex;align-items:center;gap:12px}
  .brand-mark{width:16px;height:16px;border-radius:50%;background:var(--gold)}
  .brand-name{font-family:'Rubik',sans-serif;font-weight:600;font-size:50px;letter-spacing:2px;color:var(--gold);line-height:1}
  .brand-sub{position:absolute;left:49px;top:116px;font-family:'Rubik',sans-serif;font-weight:500;font-size:14px;letter-spacing:1.6px;color:var(--white)}
  .brand-tag{position:absolute;left:48px;top:136px;font-family:'Rubik',sans-serif;font-weight:500;font-size:10.5px;letter-spacing:2.2px;color:var(--gold)}
  .headline{position:absolute;left:47px;top:173px;font-family:'Rubik',sans-serif;font-weight:600;font-size:34px;line-height:41px;color:var(--yellow)}
  .headline .place{color:var(--white)}
  .intro{position:absolute;left:45px;top:311px;width:380px;font-family:'Roboto',sans-serif;font-weight:400;font-size:23px;line-height:31px;color:var(--white)}
  .motto{position:absolute;left:42px;top:466px;font-family:'Audiowide',sans-serif;font-size:32px;color:var(--navy);transform:rotate(-5.6deg);transform-origin:left bottom;white-space:nowrap}

  /* Services / Why */
  .columns{position:absolute;left:0;top:525px;width:848px;height:325px}
  .col-head{position:absolute;top:0;height:76px;background:var(--cream)}
  .col-head h2{font-family:'Oxanium',sans-serif;font-weight:600;font-size:31.5px;letter-spacing:1px;color:var(--ink);position:absolute;top:19px}
  .col-services .col-head{left:0;width:403px}
  .col-services .col-head h2{left:41px}
  .col-why .col-head{left:405px;width:443px}
  .col-why .col-head h2{left:34px}
  .divider{position:absolute;left:402px;top:0;width:2px;height:325px;background:var(--gold-dark)}
  .list{position:absolute;top:101px;list-style:none}
  .col-services .list{left:48px}
  .col-why .list{left:446px}
  .list li{position:relative;padding-left:29px;font-weight:300;font-size:23.7px;line-height:37.7px;color:var(--ink);white-space:nowrap}
  .list li::before{content:"";position:absolute;left:0;top:13px;width:13px;height:13px;border-radius:50%;background:var(--gold-dark)}

  /* Report strip */
  .report-strip{position:absolute;left:0;top:850px;width:848px;height:57px;background:linear-gradient(90deg,var(--gold-dark) 0%,#c99d3e 70%,var(--gold-light) 100%);display:flex;align-items:center;padding-left:31px}
  .report-strip p{font-family:'Audiowide',sans-serif;font-size:22.5px;color:var(--white);white-space:nowrap}

  /* Integration */
  .integration{position:absolute;left:0;top:907px;width:848px;height:209px}
  .integration-art{position:absolute;left:0;top:0}
  .integration h2{position:absolute;left:355px;top:22px;font-family:'Oxanium',sans-serif;font-weight:600;font-size:28px;color:var(--ink);letter-spacing:0.3px;white-space:nowrap}
  .integration p{position:absolute;left:355px;top:66px;width:480px;font-weight:300;font-size:22.5px;line-height:31px;color:var(--ink)}

  /* Contact bar */
  .contact{position:absolute;left:0;top:1116px;width:848px;height:84px;background:var(--navy)}
  .contact-item{position:absolute;top:26px;display:flex;align-items:center;gap:10px;font-weight:500;font-size:25.5px;color:var(--white);white-space:nowrap}
  .contact-phone{left:28px}
  .contact-mail{left:278px}
  .contact-place{left:592px}
  .contact-item svg{flex:none}
</style>
</head>
<body>
<main class="flyer">

  <section class="hero">
    <svg class="hero-art" width="848" height="530" viewBox="0 0 848 530">
      <defs>
        <linearGradient id="bandGold" x1="0" y1="0" x2="1" y2="0">
          <stop offset="0" stop-color="#d9b15a"/>
          <stop offset="0.5" stop-color="#eed08a"/>
          <stop offset="1" stop-color="#e7c779"/>
        </linearGradient>
        <linearGradient id="workshopTone" x1="0" y1="0" x2="1" y2="1">
          <stop offset="0" stop-color="#e6ebf0"/>
          <stop offset="0.55" stop-color="#aab6c4"/>
          <stop offset="1" stop-color="#6c7c90"/>
        </linearGradient>
        <linearGradient id="circuitTone" x1="0" y1="0" x2="1" y2="1">
          <stop offset="0" stop-color="#b86a2a"/>
          <stop offset="0.45" stop-color="#2d4a5e"/>
          <stop offset="1" stop-color="#152a3a"/>
        </linearGradient>
      </defs>
      <polygon points="0,450 480,400 620,420 660,478 0,532" fill="url(#bandGold)"/>
      <path d="M590 0 L848 0 L848 180 L700 420 Q655 455 605 432 L462 335 Q402 290 438 222 Z" fill="url(#workshopTone)" stroke="var(--gold)" stroke-width="9" role="img" aria-label="Photo: technician in white coveralls working on the door of a silver car in a workshop"/>
      <path d="M848 185 L848 410 L745 492 Q705 515 662 490 L606 442 Q575 398 604 356 L718 205 Q758 172 805 180 Z" fill="url(#circuitTone)" stroke="var(--gold)" stroke-width="9" role="img" aria-label="Photo: gloved hands working on a vehicle circuit board and wiring"/>
    </svg>

    <div class="brand">
      <span class="brand-mark"></span>
      <span class="brand-name">R-VOX</span>
    </div>
    <div class="brand-sub">AUTOMOTIVE SOLUTIONS</div>
    <div class="brand-tag">ADAS DIAGNOSTICS MECHANICAL</div>

    <h1 class="headline">Mobile ADAS<br>Calibration Service<br><span class="place">in Sunvale, Arizona!</span></h1>
    <p class="intro">Accurate Diagnostics, Advanced<br>Calibrations, and Reliable<br>Solutions</p>
    <p class="motto">Locally owned and operated</p>
  </section>

  <section class="columns">
    <div class="col-services">
      <div class="col-head"><h2>SERVICES OFFERED</h2></div>
      <ul class="list">
        <li>Mobile ADAS Calibrations</li>
        <li>OEM Diagnostic Tools</li>
        <li>Mechanical Repairs</li>
        <li>Wiring repairs</li>
        <li>Pigtails</li>
      </ul>
    </div>
    <div class="divider"></div>
    <div class="col-why">
      <div class="col-head"><h2>WHY CHOOSE US</h2></div>
      <ul class="list">
        <li>AutoCert certified Technicians</li>
        <li>State-of-the-Art Equipment</li>
        <li>Convenient Mobile Services</li>
        <li>Dealership alternative.</li>
        <li>We help speed up your cycle time.</li>
      </ul>
    </div>
  </section>

  <div class="report-strip"><p>Include a complimentary CalibroLook.com report with each job</p></div>

  <section class="integration">
    <svg class="integration-art" width="330" height="209" viewBox="0 0 330 209">
      <defs>
        <linearGradient id="engineTone" x1="0" y1="0" x2="1" y2="1">
          <stop offset="0" stop-color="#c98a4a"/>
          <stop offset="0.5" stop-color="#4a4f58"/>
          <stop offset="1" stop-color="#262a33"/>
        </linearGradient>
      </defs>
      <path d="M0 0 L268 0 Q335 100 312 209 L0 209 Z" fill="var(--gold-dark)"/>
      <path d="M0 0 L250 0 Q312 100 290 209 L0 209 Z" fill="url(#engineTone)" role="img" aria-label="Photo: mechanic's hands working on a car engine"/>
    </svg>
    <h2>REPAIRVAULT INTEGRATION</h2>
    <p>Our CalibroLook.com reports link directly with RepairVault to justify ADAS needs. Ensure your customers vehicle's advanced systems are calibrated correctly and safely.</p>
  </section>

  <footer class="contact">
    <div class="contact-item contact-phone">
      <svg width="26" height="28" viewBox="0 0 24 24"><path d="M6.6 2.5 9.3 6.4c.4.6.3 1.3-.2 1.8L7.6 9.6c1 2.6 3.6 5.4 6.6 6.8l1.5-1.4c.5-.5 1.2-.6 1.8-.2l3.8 2.6c.6.4.8 1.2.4 1.8l-1.5 2.3c-.5.7-1.3 1-2.1.8C9.9 20.6 3.6 14.3 2.1 6.5c-.2-.8.1-1.6.8-2.1l2-1.5c.5-.4 1.3-.3 1.7.2Z" fill="var(--gold)"/></svg>
      <span>(555) 013-4872</span>
    </div>
    <div class="contact-item contact-mail">
      <svg width="30" height="22" viewBox="0 0 30 22"><rect x="1" y="1" width="28" height="20" fill="none" stroke="var(--gold)" stroke-width="2"/><path d="M1 1 15 12 29 1M1 21 11 10M29 21 19 10" fill="none" stroke="var(--gold)" stroke-width="2"/></svg>
      <span>Milo@r-voxauto.com</span>
    </div>
    <div class="contact-item contact-place">
      <svg width="22" height="30" viewBox="0 0 22 30"><path d="M11 1C5.5 1 1 5.4 1 10.9 1 18 11 29 11 29s10-11 10-18.1C21 5.4 16.5 1 11 1Z" fill="var(--gold)"/><circle cx="11" cy="10.5" r="4" fill="var(--navy)"/></svg>
      <span>Sunvale, Arizona</span>
    </div>
  </footer>

</main>
</body>
</html>
```